Varko label design

Redesign cafe range label for lightly carbonated fruit sodas.
Existing label has not worked in the market place and needs to appeal to 18-40 year olds with an active healthy lifestyle.

Product will remain in current 330ml glass bottle and flavour profile will include current range, sparkling water. It is preferred to maintain a body label only but will consider neck label as well. No over cap concepts will be considered..

Attached final shows brand progress. It has lost its way and needs reinvigorating.

Reason: I have extended the deadline to get proper feed back from others on the designs. Thank you all for your submissions so far. Tom

```html
<!DOCTYPE html>
<html lang="en">
<head>
<meta charset="utf-8">
<title>Varko label design</title>
<link href="https://fonts.googleapis.com/css2?family=Fondamento&display=swap" rel="stylesheet">
<style>
  :root {
    --label-pink: #e5008f;
    --ink: #2a2a2a;
    --ribbon-orange: #f79a43;
    --flavour-pink: #e5008f;
  }
  html, body {
    margin: 0;
    padding: 0;
    overflow: hidden;
  }
  .label {
    position: relative;
    width: 1200px;
    height: 999px;
    background: var(--label-pink);
    font-family: "Fondamento", cursive;
    color: var(--ink);
    overflow: hidden;
  }
  .brand {
    position: absolute;
    left: 0;
    top: 375px;
    width: 1200px;
    display: flex;
    align-items: center;
    justify-content: center;
    gap: 18px;
  }
  .brand-dot {
    width: 34px;
    height: 34px;
    border-radius: 50%;
    background: var(--ink);
  }
  .brand-name {
    font-size: 96px;
    line-height: 1;
    color: var(--ink);
  }
  .volume {
    position: absolute;
    left: 340px;
    top: 548px;
    font-size: 24px;
    font-style: italic;
  }
  .tagline {
    position: absolute;
    left: 0;
    top: 588px;
    width: 1200px;
    text-align: center;
    font-size: 50px;
    line-height: 1;
  }
  .ribbon {
    position: absolute;
    left: 0;
    top: 0;
  }
  .flavour {
    position: absolute;
    left: 335px;
    top: 685px;
    font-size: 13px;
    letter-spacing: 0.5px;
    color: var(--flavour-pink);
  }
  .carbonation {
    position: absolute;
    left: 684px;
    top: 665px;
    font-size: 16px;
    font-style: italic;
  }
</style>
</head>
<body>
  <main class="label">
    <div class="brand">
      <span class="brand-dot"></span>
      <span class="brand-name">Varko</span>
    </div>
    <div class="volume">330ml</div>
    <h1 class="tagline" style="margin:0;font-weight:400;">Fresh Tasty Fruit Drink</h1>
    <svg class="ribbon" width="1200" height="999" viewBox="0 0 1200 999" aria-hidden="true">
      <polygon points="287,682 720,687 915,668 875,700 720,690 310,705" fill="var(--ribbon-orange)"/>
    </svg>
    <div class="flavour">RASPBERRY &amp; CRANBERRY</div>
    <div class="carbonation">“Lightly Carbonated”</div>
  </main>
</body>
</html>
```